Best in class business looking for best in class stationery that accurately reflects the brand image we are trying to build as the brand expands throughout the country. The Varying items should be an eye catching design that makes even the simplest letter or small business card stand out in the crowd.

Target Market(s)

Professionals

Industry/Entity Type

Real Estate

Other font styles liked:
• See atttached logo

Requirements
Must have
• Letterhead
• Business cards
• Envelopes
• Labels for larger mailings
Nice to have
• Folders
• Notebook
Should not have
• Stale design elements

```html
<!DOCTYPE html>
<html lang="en">
<head>
<meta charset="utf-8">
<title>Ridgeline Property Group – Stationery</title>
<link href="https://fonts.googleapis.com/css2?family=Didact+Gothic&family=Arimo:wght@400;700&display=swap" rel="stylesheet">
<style>
  :root{
    --bg:#e2e2e2;
    --paper:#f5f5f5;
    --white:#ffffff;
    --navy:#283579;
    --blue:#2f55a7;
    --ink:#222222;
    --muted:#555555;
    --rule:#b9bfd2;
    --ring:#3a3a3a;
  }
  *{box-sizing:border-box;margin:0;padding:0}
  html,body{width:1200px;height:737px;overflow:hidden;background:var(--bg)}
  body{position:relative;font-family:"Arimo",Arial,sans-serif;color:var(--ink)}
  .item{position:absolute;box-shadow:0 1px 3px rgba(0,0,0,.18)}
  .brand{display:flex;align-items:center;justify-content:center;gap:4px;font-family:"Didact Gothic",sans-serif;color:var(--navy);white-space:nowrap;letter-spacing:.06em;text-transform:uppercase}
  .brand .mark{width:.9em;height:.9em;background:currentColor;flex:none}
  .brand.light{color:var(--white)}
  .gothic{font-family:"Didact Gothic",sans-serif}

  /* letterhead */
  .letterhead{left:33px;top:36px;width:350px;height:496px;background:var(--paper)}
  .letterhead .brand{position:absolute;top:58px;left:0;right:0;font-size:8px}
  .letter-body{position:absolute;left:26px;top:155px;width:302px;font-size:5.6px;line-height:1.35;color:var(--ink)}
  .letter-body p{margin-bottom:6px}
  .letter-body .salutation{margin-bottom:18px}
  .signoff{position:absolute;left:26px;top:324px;font-size:5.6px;line-height:1.4}
  .signature{position:absolute;left:84px;top:333px;width:50px;height:16px;background:linear-gradient(90deg,rgba(60,90,170,.25),rgba(60,90,170,.1));border-radius:3px}
  .letter-foot{position:absolute;left:0;bottom:0;width:100%;height:26px;background:linear-gradient(90deg,var(--navy),var(--blue));color:var(--white);font-size:5.4px;font-family:"Didact Gothic",sans-serif}
  .letter-foot .contacts{position:absolute;left:22px;top:3px;line-height:8px}
  .letter-foot .web{position:absolute;right:14px;top:2px;text-align:right;line-height:8px}
  .letter-foot .brand{position:absolute;left:155px;top:8px;font-size:6px}
  .ico{display:inline-block;width:5px;height:5px;background:var(--white);border-radius:1px;margin-right:3px;vertical-align:middle}

  /* folder */
  .folder{left:406px;top:36px;width:351px;height:496px;background:linear-gradient(90deg,var(--navy) 50%,var(--blue) 50%)}
  .folder .brand{position:absolute;top:266px;left:0;right:0;font-size:17px}
  .folder .sub{position:absolute;top:288px;left:0;right:0;text-align:center;color:var(--white);font-family:"Didact Gothic",sans-serif;font-size:8px;letter-spacing:.5em}

  /* label */
  .label{left:39px;top:546px;width:343px;height:154px;background:var(--paper)}
  .label .brand{position:absolute;left:17px;top:42px;font-size:8px;justify-content:flex-start}
  .label .addr{position:absolute;left:17px;top:57px;font-size:5.6px;line-height:7px;color:var(--muted)}
  .band{position:absolute;left:0;bottom:0;width:100%;background:linear-gradient(90deg,var(--navy),var(--blue))}
  .label .band{height:9px}

  /* envelope */
  .envelope{left:408px;top:546px;width:343px;height:154px;background:var(--paper)}
  .envelope svg{position:absolute;left:0;top:0}
  .envelope .brand{position:absolute;top:20px;left:0;right:0;font-size:8px}
  .envelope .web{position:absolute;top:41px;left:0;right:0;text-align:center;font-size:6.4px;font-style:normal;color:var(--muted)}

  /* business cards */
  .card-front{left:810px;top:125px;width:106px;height:61px;background:var(--white)}
  .card-front .brand{position:absolute;top:16px;left:0;right:0;font-size:4px}
  .card-front .name{position:absolute;top:32px;left:0;right:0;text-align:center;font-size:3px;color:var(--navy)}
  .card-front .strip{position:absolute;left:0;bottom:0;width:100%;height:15px;background:var(--navy);color:var(--white);font-size:2.4px;line-height:3.4px}
  .card-front .strip .l{position:absolute;left:3px;top:2px}
  .card-front .strip .r{position:absolute;right:3px;top:2px;text-align:right}
  .card-back{left:810px;top:201px;width:106px;height:60px;background:linear-gradient(90deg,var(--navy) 52%,var(--blue) 52%)}
  .card-back .brand{position:absolute;left:14px;top:26px;font-size:5px}
  .card-back .web{position:absolute;left:60px;top:28px;font-size:2.6px;color:var(--white)}

  /* mailing label card */
  .mailer{left:975px;top:134px;width:201px;height:126px;background:var(--white)}
  .mailer .brand{position:absolute;left:12px;top:34px;font-size:6px}
  .mailer .addr{position:absolute;left:13px;top:56px;font-size:5px;line-height:7.6px;color:var(--muted)}
  .mailer .dot{display:inline-block;width:4px;height:4px;background:var(--navy);border-radius:50%;margin-right:3px}
  .mailer .to{position:absolute;left:108px;top:41px;font-size:6.4px;color:var(--navy);letter-spacing:.05em}
  .mailer .line{position:absolute;left:109px;width:75px;border-top:.7px solid var(--rule)}
  .mailer .band{height:8px}

  /* notebooks */
  .rings{position:absolute;left:4px;right:4px;top:-6px;height:10px;background:repeating-linear-gradient(90deg,var(--ring) 0 1.4px,transparent 1.4px 7px)}
  .notebook{background:linear-gradient(90deg,var(--navy) 50%,var(--blue) 50%)}
  .nb-small{left:782px;top:294px;width:171px;height:119px}
  .nb-small .brand{position:absolute;left:0;right:0;top:79px;font-size:8px}
  .nb-large{left:774px;top:458px;width:186px;height:239px}
  .nb-large .brand{position:absolute;left:0;right:0;top:133px;font-size:8.5px}
  .notepad{background:var(--white)}
  .np-small{left:986px;top:294px;width:171px;height:117px}
  .np-large{left:983px;top:458px;width:187px;height:239px}
  .notepad .brand{position:absolute;left:0;right:0;font-size:6px}
  .notepad .rule{position:absolute;left:13px;right:13px;border-top:.7px solid var(--rule)}
  .notepad .web{position:absolute;left:0;right:0;text-align:center;font-size:4.8px;letter-spacing:.15em;color:var(--navy)}
  .np-small .band{height:9px}
  .np-large .band{height:9px}
</style>
</head>
<body>

<!-- Letterhead -->
<section class="item letterhead">
  <div class="brand"><span class="mark"></span>Ridgeline Property Group</div>
  <div class="letter-body">
    <p class="salutation">Dear Mr. Smith,</p>
    <p>Lorem ipsum dolor sit amet, consectetur adipiscing elit. Donec orci purus, luctus vitae dignissim eu, iaculis sed purus. Vivamus faucibus, ipsum nec aliquet viverra, leo mauris condimentum ligula, sit amet sagittis enim ligula quis arcu. Nam egestas tortor id nisi porttitor mattis. In tortor ante, ultricies in suscipit a, tempus non massa. Vivamus et auctor mi.</p>
    <p>Fusce vel massa nulla. Phasellus nec eros mauris, et scelerisque orci. Donec malesuada orci vitae nulla accumsan porta a id massa. Quisque accumsan iaculis magna sit amet fringilla. Maecenas consequat, magna eget tincidunt semper, odio nibh rutrum mi, id feugiat ante nisi eu risus. Vestibulum nunc orci, rhoncus a placerat in, ultricies in mi. Cras mattis varius eros, vel fringilla nisi suscipit eget.</p>
    <p>Quisque scelerisque sagittis nulla at porttitor. Mauris a justo et tellus interdum tristique. Sed id augue vitae urna euismod commodo aliquet a quam. Pellentesque arcu velit, cursus et molestie at, consequat et diam. Nullam erat sem, rhoncus id ullamcorper vitae, rhoncus et arcu. In ultricies ultricies nulla, ut rutrum nisi iaculis at. Donec eu magna a metus ornare faucibus.</p>
    <p>Fusce aliquet faucibus ultricies. Morbi semper, est id tincidunt gravida, sem arcu adipiscing lacus, ac bibendum nulla leo eu purus. Quisque nec diam sed risus consectetur a cursus quis nibh. Vestibulum id purus lorem.</p>
  </div>
  <div class="signoff">Daniel Reyes<br>Co-Founder &amp; CEO</div>
  <div class="signature" role="img" aria-label="Handwritten signature of Daniel Reyes"></div>
  <div class="letter-foot">
    <div class="contacts"><span class="ico"></span>555 210 4871<br><span class="ico"></span>555 318 6620<br><span class="ico"></span>555 402 7395</div>
    <div class="brand light"><span class="mark"></span>Ridgeline</div>
    <div class="web">hello@ridgelinegroup.com<br>www.ridgelinegroup.com<br>1420 Cedar Hollow Road, Boise, Idaho 83702</div>
  </div>
</section>

<!-- Folder -->
<section class="item folder">
  <div class="brand light"><span class="mark"></span>Ridgeline Property Group</div>
</section>

<!-- Return address label -->
<section class="item label">
  <div class="brand"><span class="mark"></span>Ridgeline Property Group</div>
  <div class="addr gothic">1420 Cedar Hollow Road<br>Boise, Idaho 83702</div>
  <div class="band"></div>
</section>

<!-- Envelope -->
<section class="item envelope">
  <svg width="343" height="154" viewBox="0 0 343 154" aria-hidden="true">
    <path d="M2 0 Q6 40 30 56 L310 56 Q334 40 341 0" fill="#f8f8f8" stroke="#cfcfcf" stroke-width="1"/>
  </svg>
  <div class="brand"><span class="mark"></span>Ridgeline</div>
  <div class="web">www.ridgelinegroup.com</div>
</section>

<!-- Business cards -->
<section class="item card-front">
  <div class="brand"><span class="mark"></span>Ridgeline Property Group</div>
  <div class="name">MARK ELLISON · CEO FOUNDER</div>
  <div class="strip gothic">
    <div class="l">1420 CEDAR HOLLOW RD<br>BOISE, IDAHO 83702<br>WWW.RIDGELINEGROUP.COM</div>
    <div class="r">TEL 555 210 4871<br>MOB 555 318 6620<br>FAX 555 402 7395</div>
  </div>
</section>
<section class="item card-back">
  <div class="brand light"><span class="mark"></span></div>
  <div class="web gothic">RIDGELINEGROUP.COM</div>
</section>

<!-- Mailing label -->
<section class="item mailer">
  <div class="brand"><span class="mark"></span>Ridgeline Property Group</div>
  <div class="addr gothic">
    1420 Cedar Hollow Road<br>Boise, Idaho 83702<br>
    <span class="dot"></span>555 210 4871<br>
    <span class="dot"></span>555 318 6620<br>
    <span class="dot"></span>555 402 7395<br>
    <span class="dot"></span>hello@ridgelinegroup.com<br>
    <span class="dot"></span>www.ridgelinegroup.com
  </div>
  <div class="to">To :</div>
  <div class="line" style="top:61px"></div>
  <div class="line" style="top:77px"></div>
  <div class="line" style="top:92px"></div>
  <div class="band"></div>
</section>

<!-- Notebooks -->
<section class="item notebook nb-small">
  <div class="rings"></div>
  <div class="brand light"><span class="mark"></span>Ridgeline Property Group</div>
</section>

<section class="item notepad np-small">
  <div class="rings"></div>
  <div class="brand" style="top:24px"><span class="mark"></span>Ridgeline Property Group</div>
  <div class="rule" style="top:52px"></div>
  <div class="rule" style="top:66px"></div>
  <div class="rule" style="top:80px"></div>
  <div class="rule" style="top:94px"></div>
  <div class="web gothic" style="top:97px">www.ridgelinegroup.com</div>
  <div class="band"></div>
</section>

<section class="item notebook nb-large">
  <div class="rings"></div>
  <div class="brand light"><span class="mark"></span>Ridgeline Property Group</div>
</section>

<section class="item notepad np-large">
  <div class="rings"></div>
  <div class="brand" style="top:36px"><span class="mark"></span>Ridgeline Property Group</div>
  <div class="rule" style="top:63px"></div>
  <div class="rule" style="top:80px"></div>
  <div class="rule" style="top:96px"></div>
  <div class="rule" style="top:112px"></div>
  <div class="rule" style="top:129px"></div>
  <div class="rule" style="top:145px"></div>
  <div class="rule" style="top:161px"></div>
  <div class="rule" style="top:177px"></div>
  <div class="rule" style="top:194px"></div>
  <div class="web gothic" style="top:219px">www.ridgelinegroup.com</div>
  <div class="band"></div>
</section>

</body>
</html>
```